Healthy Snack Bar Wrapper Design

We are passionate about delivering healthy and tasty treats that are Raw, Organic, Preservative Free, Gluten Free, have No Added Sugar and No Additives!
In this project we are looking for a design for a new healthy food product to be launched soon in Australia. The packaging will be a bar wrapper made from foil that will be hot sealed, with a front and a back.
The snack is a raw, organic and healthy treat made predominantly with nuts, and will come in 3 initial flavours:
- Black Forest (Sour Cherry and Choc)
- Plum Fandango (Banana, Apricot and Blueberry)
- Zestivelle (Pineapple, Passionfruit and Kiwi)
The product name is NibbleMoss, which does not currently have a logo. We are happy to have this as a simple written component of the initial design at the top of the packaging, perhaps within an circle, square or oval.
The typeface used for the names and the main ingredients should be fun.
The overall design should be very simple and make use of minimal colours. Our preferences are to have a plain colour for the background, such as light organic brown or white, with an eye catching colour that can be used to define the flavour, but should not be too vibrant.
We do not want to have an 3 dimensional images or objects. Nor do we want to have product images and any imagery should be only to give the impression of the flavours within rather than an image of the flavour. Finally, we do not want to have gradients included in the design.
The final design should communicate healthy, tasty and fun!
Examples of inspiration designs are attached in the files.
Main Information:
- The front should comprise of the following information:
-- NibbleMoss
-- Flavour name (such as Black Forest)
-- Main Ingredients (Sour Cherry and Choc) (This is optional)
-- Portion size (60g)
-- Message (This is optional)
--- 0% Additives
--- 60% Nuts
--- 100% Natural
- The back needs to have space for the following information:
-- Nutritional Information
-- Barcode
-- Ingredients
-- Contact information
- Wrapper Dimensions
-- Width: 14cm
-- Height: 15cm
- Bar Dimensions
-- Width: 3cm
-- Height: 10cm
-- Depth: 2.5cm
Target Market(s)
People who want to have a healthy tasty treat
Colors
Designer to choose colors to be used in the design.
Requirements
Must have
- Main Information:
- - The front should comprise of the following information:
- -- NibbleMoss
- -- Flavour name (such as Black Forest)
- -- Main Ingredients (Sour Cherry and Choc) (This is optional)
- -- Portion size (60g)
- -- Message (This is optional)
- --- 0% Additives
- --- 60% Nuts
- --- 100% Natural
- - The back needs to have space for the following information:
- -- Nutritional Information
- -- Barcode
- -- Ingredients
- -- Contact information
- - Wrapper Dimensions
- -- Width: 14cm
- -- Height: 15cm
- - Bar Dimensions
- -- Width: 3cm
- -- Height: 10cm
- -- Depth: 2.5cm
Should not have
- We do not want to have an 3 dimensional images or objects. Nor do we want to have product images and any imagery should be only to give the impression of the flavours within rather than an image of the flavour. Finally, we do not want to have gradients included in the design.

```html
<!DOCTYPE html>
<html lang="en">
<head>
<meta charset="utf-8">
<title>NibbleMoss Snack Bar Wrappers</title>
<link rel="stylesheet" href="https://fonts.googleapis.com/css2?family=Amatic+SC:wght@700&family=Patrick+Hand&display=swap">
<style>
  :root {
    --backdrop: #fbf4c8;
    --foil: #a68e89;
    --foil-seal: #9a827d;
    --foil-crimp: #8c7570;
    --paper: #ffffff;
    --sun: #f2ea5a;
    --forest: #3f2a7a;
    --plum: #19468e;
    --plum-accent: #f0b431;
    --zest: #3f7428;
    --zest-accent: #dff05a;
  }
  * { margin: 0; padding: 0; box-sizing: border-box; }
  html, body { width: 1200px; height: 770px; overflow: hidden; }
  body { background: var(--backdrop); position: relative; }

  .wrapper-row { position: absolute; left: 140px; top: 107px; display: flex; gap: 40px; }
  .wrapper { width: 280px; height: 556px; display: block; }

  .foil-body { fill: var(--foil); }
  .foil-seal { fill: var(--foil-seal); }
  .brand-name { font-family: "Patrick Hand", cursive; font-size: 40px; fill: var(--paper); }
  .brand-dot { fill: var(--paper); }
  .flavour-title { font-family: "Amatic SC", cursive; font-weight: 700; font-size: 50px; fill: var(--paper); text-anchor: middle; }
  .ingredients { font-family: "Amatic SC", cursive; font-weight: 700; font-size: 23px; text-anchor: middle; }
  .message { font-family: "Amatic SC", cursive; font-weight: 700; font-size: 25px; text-anchor: middle; }
  .claims-box { fill: var(--paper); }
  .claims { font-family: "Patrick Hand", cursive; font-size: 15px; text-anchor: middle; }
  .weight { font-family: "Patrick Hand", cursive; font-size: 17px; fill: var(--paper); text-anchor: end; }

  .flavour-black-forest { --ink: var(--forest); --accent: var(--sun); }
  .flavour-plum-fandango { --ink: var(--plum); --accent: var(--plum-accent); }
  .flavour-zestivelle { --ink: var(--zest); --accent: var(--zest-accent); }

  .band-ink { fill: var(--ink); }
  .band-accent { fill: var(--accent); }
  .flavour-badge { fill: var(--ink); stroke: var(--accent); stroke-width: 6; }
  .badge-rule { stroke: var(--accent); stroke-width: 2; }
  .ingredients { fill: var(--accent); }
  .message-band { fill: var(--accent); }
  .message { fill: var(--ink); }
  .claims-box { stroke: var(--ink); stroke-width: 1.5; }
  .claims { fill: var(--ink); }
</style>
</head>
<body>
<svg width="0" height="0" style="position:absolute">
  <defs>
    <pattern id="seal-teeth-top" width="10" height="8" patternUnits="userSpaceOnUse">
      <polygon points="0,8 5,0 10,8" fill="#9a827d"/>
    </pattern>
    <pattern id="seal-teeth-bottom" width="10" height="8" patternUnits="userSpaceOnUse">
      <polygon points="0,0 5,8 10,0" fill="#9a827d"/>
    </pattern>
    <pattern id="seal-ribs" width="6" height="40" patternUnits="userSpaceOnUse">
      <rect x="0" y="0" width="1.5" height="40" fill="#8c7570"/>
    </pattern>
    <clipPath id="body-clip"><rect x="0" y="52" width="280" height="440"/></clipPath>
  </defs>
</svg>

<main class="wrapper-row">

  <!-- Black Forest -->
  <svg class="wrapper flavour-black-forest" viewBox="0 0 280 556">
    <rect x="0" y="0" width="280" height="8" fill="url(#seal-teeth-top)"/>
    <rect class="foil-seal" x="0" y="8" width="280" height="44"/>
    <rect x="0" y="16" width="280" height="28" fill="url(#seal-ribs)"/>
    <rect class="foil-body" x="0" y="52" width="280" height="440"/>
    <g clip-path="url(#body-clip)">
      <polygon class="band-accent" points="0,210 280,70 280,86 0,228"/>
      <polygon class="band-ink" points="0,420 280,250 280,278 0,450"/>
      <polygon class="band-ink" points="0,470 280,310 280,330 0,492"/>
      <polygon class="band-accent" points="40,492 280,360 280,372 62,492"/>
    </g>
    <rect class="foil-seal" x="0" y="492" width="280" height="56"/>
    <rect x="0" y="500" width="280" height="36" fill="url(#seal-ribs)"/>
    <rect x="0" y="548" width="280" height="8" fill="url(#seal-teeth-bottom)"/>

    <circle class="brand-dot" cx="40" cy="131" r="6"/>
    <text class="brand-name" x="54" y="144">NibbleMoss</text>

    <ellipse class="flavour-badge" cx="144" cy="292" rx="82" ry="98"/>
    <text class="flavour-title" x="144" y="246">BLACK</text>
    <text class="flavour-title" x="144" y="292">FOREST</text>
    <line class="badge-rule" x1="104" y1="305" x2="184" y2="305"/>
    <text class="ingredients" x="144" y="328">SOUR</text>
    <text class="ingredients" x="144" y="350">CHERRY</text>
    <text class="ingredients" x="144" y="372">&amp; CHOC</text>

    <rect class="message-band" x="64" y="384" width="168" height="34"/>
    <text class="message" x="148" y="410">HEALTHIER &amp; BETTER</text>
    <rect class="claims-box" x="98" y="420" width="96" height="56"/>
    <text class="claims" x="146" y="437">0% ADDITIVES</text>
    <text class="claims" x="146" y="453">100% NATURAL</text>
    <text class="claims" x="146" y="469">60% NUTS</text>
    <text class="weight" x="250" y="484">60g</text>
  </svg>

  <!-- Plum Fandango -->
  <svg class="wrapper flavour-plum-fandango" viewBox="0 0 280 556">
    <rect x="0" y="0" width="280" height="8" fill="url(#seal-teeth-top)"/>
    <rect class="foil-seal" x="0" y="8" width="280" height="44"/>
    <rect x="0" y="16" width="280" height="28" fill="url(#seal-ribs)"/>
    <rect class="foil-body" x="0" y="52" width="280" height="440"/>
    <g clip-path="url(#body-clip)">
      <polygon class="band-ink" points="30,300 250,52 280,52 280,70 60,320"/>
      <polygon class="band-accent" points="0,470 280,210 280,240 0,500"/>
      <polygon class="band-accent" points="0,492 0,520 40,492"/>
    </g>
    <rect class="foil-seal" x="0" y="492" width="280" height="56"/>
    <rect x="0" y="500" width="280" height="36" fill="url(#seal-ribs)"/>
    <rect x="0" y="548" width="280" height="8" fill="url(#seal-teeth-bottom)"/>

    <circle class="brand-dot" cx="40" cy="131" r="6"/>
    <text class="brand-name" x="54" y="144">NibbleMoss</text>

    <ellipse class="flavour-badge" cx="144" cy="292" rx="82" ry="98"/>
    <text class="flavour-title" x="144" y="246">PLUM</text>
    <text class="flavour-title" x="144" y="292">FANDANGO</text>
    <line class="badge-rule" x1="104" y1="305" x2="184" y2="305"/>
    <text class="ingredients" x="144" y="328">BANANA,</text>
    <text class="ingredients" x="144" y="350">APRICOT</text>
    <text class="ingredients" x="144" y="372">&amp; BLUEBERRY</text>

    <rect class="message-band" x="70" y="384" width="156" height="34"/>
    <text class="message" x="148" y="410">VEGAN FRIENDLY</text>
    <rect class="claims-box" x="98" y="420" width="96" height="56"/>
    <text class="claims" x="146" y="437">0% ADDITIVES</text>
    <text class="claims" x="146" y="453">100% NATURAL</text>
    <text class="claims" x="146" y="469">60% NUTS</text>
    <text class="weight" x="250" y="484">60g</text>
  </svg>

  <!-- Zestivelle -->
  <svg class="wrapper flavour-zestivelle" viewBox="0 0 280 556">
    <rect x="0" y="0" width="280" height="8" fill="url(#seal-teeth-top)"/>
    <rect class="foil-seal" x="0" y="8" width="280" height="44"/>
    <rect x="0" y="16" width="280" height="28" fill="url(#seal-ribs)"/>
    <rect class="foil-body" x="0" y="52" width="280" height="440"/>
    <g clip-path="url(#body-clip)">
      <polygon class="band-accent" points="0,260 280,92 280,108 0,276"/>
      <polygon class="band-accent" points="0,300 280,200 280,212 0,312"/>
      <polygon class="band-ink" points="0,472 280,290 280,306 0,488"/>
      <polygon class="band-ink" points="70,492 280,340 280,352 88,492"/>
    </g>
    <rect class="foil-seal" x="0" y="492" width="280" height="56"/>
    <rect x="0" y="500" width="280" height="36" fill="url(#seal-ribs)"/>
    <rect x="0" y="548" width="280" height="8" fill="url(#seal-teeth-bottom)"/>

    <circle class="brand-dot" cx="40" cy="131" r="6"/>
    <text class="brand-name" x="54" y="144">NibbleMoss</text>

    <ellipse class="flavour-badge" cx="144" cy="292" rx="82" ry="98"/>
    <text class="flavour-title" x="144" y="278" textLength="146" lengthAdjust="spacingAndGlyphs">ZESTIVELLE</text>
    <line class="badge-rule" x1="104" y1="305" x2="184" y2="305"/>
    <text class="ingredients" x="144" y="328">PINEAPPLE,</text>
    <text class="ingredients" x="144" y="350">PASSIONFRUIT</text>
    <text class="ingredients" x="144" y="372">&amp; KIWI</text>

    <rect class="message-band" x="92" y="384" width="112" height="34"/>
    <text class="message" x="148" y="410">YUMMIE!!!</text>
    <rect class="claims-box" x="98" y="420" width="96" height="56"/>
    <text class="claims" x="146" y="437">0% ADDITIVES</text>
    <text class="claims" x="146" y="453">100% NATURAL</text>
    <text class="claims" x="146" y="469">60% NUTS</text>
    <text class="weight" x="250" y="484">60g</text>
  </svg>

</main>
</body>
</html>
```